Flyer Design

We are a new dental centre opening i would like to do a letter drop advising of our services, hours and location.

In addition to the flyer i would like to create a package for business cards, letter head and also magnets. With our colour theme being as in our logo.

Target Market(s)

Familys and adult females

Industry/Entity Type

Dental

```html
<!DOCTYPE html>
<html lang="en">
<head>
<meta charset="utf-8">
<title>Kova Medical Centre – Grand Opening Flyer</title>
<link rel="stylesheet" href="https://fonts.googleapis.com/css2?family=Cinzel:wght@600&family=Tinos:wght@400;700&family=Arimo:wght@700&display=swap">
<style>
  :root {
    --brand-green: #3db542;
    --ribbon-light: #3aa548;
    --ribbon-dark: #157a3a;
    --ribbon-back: #0f5a2c;
    --deep-teal: #1d5a4a;
    --wave-dark: #1f5c4c;
    --wave-mid: #8cc63f;
    --panel-top: #9ccd3a;
    --panel-mid: #56b030;
    --panel-bottom: #3f9f2a;
    --paper: #ffffff;
    --photo-warm: #e9d7c6;
    --photo-cool: #9fc7d3;
  }
  * { margin: 0; padding: 0; box-sizing: border-box; }
  html, body { width: 1200px; height: 2652px; overflow: hidden; background: var(--paper); }
  .flyer { position: relative; width: 1200px; height: 2652px; overflow: hidden; background: var(--paper); }

  .family-photo {
    position: absolute; left: 0; top: 0; width: 1200px; height: 442px;
    background: linear-gradient(100deg, var(--photo-warm) 0%, #f3ece4 35%, #d9e6e0 65%, var(--photo-cool) 100%);
  }

  .brand-name {
    position: absolute; left: 0; top: 740px; width: 1200px; text-align: center;
    font-family: "Tinos", serif; font-weight: 700; color: var(--brand-green);
    font-size: 100px; line-height: 120px;
  }

  .opening-ribbon { position: absolute; left: 150px; top: 1050px; width: 900px; height: 220px; }
  .opening-ribbon__text {
    position: absolute; left: 150px; top: 1074px; width: 900px; text-align: center;
    font-family: "Cinzel", serif; font-weight: 600; color: var(--paper);
    font-size: 74px; line-height: 78px;
  }

  .service-headline {
    position: absolute; left: 0; top: 1352px; width: 1200px; text-align: center;
    font-family: "Cinzel", serif; font-weight: 600; color: var(--deep-teal);
    font-size: 63px; line-height: 78px;
  }

  .contact-panel { position: absolute; left: 0; top: 1580px; width: 1200px; height: 1072px; }

  .contact-details {
    position: absolute; left: 0; top: 2064px; width: 1200px; text-align: center; color: var(--paper);
    font-family: "Tinos", serif;
  }
  .contact-details__intro { font-size: 54px; line-height: 62px; }
  .contact-details__address { font-size: 54px; line-height: 66px; font-weight: 700; }
  .contact-details__phone { font-family: "Arimo", sans-serif; font-weight: 700; font-size: 56px; line-height: 64px; margin-top: 52px; }
  .contact-details__cta { font-size: 52px; line-height: 60px; }
  .contact-details__offer { font-size: 38px; line-height: 44px; margin-top: 84px; }
  .contact-details__offer b { font-weight: 700; }
</style>
</head>
<body>
<main class="flyer">
  <div class="family-photo" role="img" aria-label="Photo of a smiling family of four relaxing together on a sofa"></div>

  <div class="brand-name">Kova Medical Centre</div>

  <svg class="opening-ribbon" viewBox="0 0 900 220" aria-hidden="true">
    <defs>
      <linearGradient id="ribbonFill" x1="0" y1="0" x2="0" y2="1">
        <stop offset="0" stop-color="var(--ribbon-light)"/>
        <stop offset="1" stop-color="var(--ribbon-dark)"/>
      </linearGradient>
    </defs>
    <polygon points="0,40 80,40 80,215 0,215 30,128" fill="var(--ribbon-back)"/>
    <polygon points="900,40 820,40 820,215 900,215 870,128" fill="var(--ribbon-back)"/>
    <rect x="46" y="14" width="808" height="180" fill="#000" opacity="0.25"/>
    <polygon points="36,8 864,8 848,188 52,188" fill="url(#ribbonFill)"/>
    <polygon points="50,20 850,20 836,176 64,176" fill="none" stroke="var(--paper)" stroke-width="4"/>
  </svg>
  <div class="opening-ribbon__text">Grand Opening<br>2014</div>

  <div class="service-headline">Same Day<br>Urgent Care Appointment</div>

  <svg class="contact-panel" viewBox="0 0 1200 1072" aria-hidden="true">
    <defs>
      <radialGradient id="panelFill" cx="0.45" cy="0.35" r="0.8">
        <stop offset="0" stop-color="var(--panel-top)"/>
        <stop offset="0.55" stop-color="var(--panel-mid)"/>
        <stop offset="1" stop-color="var(--panel-bottom)"/>
      </radialGradient>
      <linearGradient id="waveBand" x1="0" y1="0" x2="1" y2="0">
        <stop offset="0" stop-color="var(--wave-dark)"/>
        <stop offset="0.45" stop-color="var(--wave-mid)"/>
        <stop offset="1" stop-color="var(--wave-dark)"/>
      </linearGradient>
    </defs>
    <path d="M0,310 C180,420 420,470 700,300 C900,180 1080,40 1200,0 L1200,1072 L0,1072 Z" fill="var(--wave-dark)"/>
    <path d="M0,330 C190,440 430,480 710,320 C910,200 1080,80 1200,48 L1200,1072 L0,1072 Z" fill="url(#waveBand)"/>
    <path d="M0,350 C200,460 440,500 720,340 C920,225 1085,120 1200,96 L1200,1072 L0,1072 Z" fill="url(#panelFill)"/>
  </svg>

  <div class="contact-details">
    <div class="contact-details__intro">Located Within the Newly Renovated</div>
    <div class="contact-details__address">Kova Medical Centre 2047<br>Linden Park Rd Ashvale</div>
    <div class="contact-details__phone">Ph: 9000 4127</div>
    <div class="contact-details__cta">For an appointment</div>
    <div class="contact-details__offer">Opening Special Sports Mouthguards <b>$80.00</b></div>
  </div>
</main>
</body>
</html>
```